Wooden Floor Website

I'd like a Modern and crisp site with emphasis on the site being easy to navigate through - services that we offer, gallery of previous work, history, who we are, contact, etc
https://tmqrvx8219067-my.dokshelfbox.net/:b:/g/personal/marcus_bellhaven_co_uk/QWT7K2_pmRsNaHXdovtYBeLWCKjuP9e3F6kRMZbqUwnPzs

Coding

Coded - Design and coding required

Number of Pages Required

5+ page

Requirements
Must have
• Word Press Site

```html
<!DOCTYPE html>
<html lang="en">
<head>
<meta charset="utf-8">
<title>Bellhaven – Wooden Floors</title>
<link href="https://fonts.googleapis.com/css2?family=IBM+Plex+Sans:ital,wght@0,400;0,500;0,600;1,400;1,600;1,700&display=swap" rel="stylesheet">
<style>
:root{
  --white:#ffffff;
  --ink:#1f1f1f;
  --text:#444444;
  --muted:#7a7a7a;
  --soft:#f6f6f6;
  --line:#e4e4e4;
  --hero-a:#dcdddf;
  --hero-b:#a9a8a5;
  --floor:#564c45;
  --accent:#b5d31c;
  --accent-dark:#8fae0c;
}
*{box-sizing:border-box;margin:0;padding:0}
html,body{width:1200px;height:839px;overflow:hidden;background:var(--white)}
body{font-family:"IBM Plex Sans",Arial,sans-serif;color:var(--text);position:relative}

.site-nav{position:absolute;top:0;left:0;width:1200px;height:36px;background:var(--white);display:flex;justify-content:flex-end;align-items:center;padding-right:28px;gap:22px;z-index:3}
.site-nav a{font-size:10px;font-weight:500;letter-spacing:.6px;color:var(--ink);text-decoration:none}
.site-nav a.is-active{border-bottom:2px solid var(--ink);padding-bottom:2px}
.site-nav svg{width:13px;height:13px}

.hero{position:absolute;top:36px;left:0;width:1200px;height:324px;overflow:hidden}
.hero-photo{position:absolute;inset:0;
  background:
    radial-gradient(ellipse 260px 200px at 930px 120px,rgba(255,255,255,.55),rgba(255,255,255,0) 70%),
    linear-gradient(180deg,var(--hero-a) 0%,#cfd0d1 50%,var(--hero-b) 68%,#7a716a 82%,var(--floor) 100%)}
.brand-name{position:absolute;left:180px;top:84px;font-size:30px;font-weight:600;letter-spacing:5px;color:#3a3a3a}
.signup{position:absolute;left:490px;top:104px;width:250px;background:rgba(120,120,120,.35);border:1px solid rgba(255,255,255,.4);padding:12px 18px 14px}
.signup h2{font-size:13px;font-weight:400;font-style:italic;color:var(--white);text-align:center;margin-bottom:10px}
.signup label{display:block;font-size:7px;color:rgba(255,255,255,.85);margin-bottom:2px}
.signup .field{font-size:8px;color:var(--white);border-bottom:1px solid rgba(255,255,255,.55);padding-bottom:3px;margin-bottom:8px}
.signup .cta{display:block;margin:10px auto 0;width:130px;height:20px;background:linear-gradient(var(--accent),var(--accent-dark));color:#1e2a00;font-size:8px;font-weight:600;text-align:center;line-height:20px;border-radius:2px}
.scroll-down{position:absolute;left:594px;top:300px;width:12px;height:8px}

.intro{position:absolute;top:360px;left:0;width:1200px;height:140px;background:var(--white)}
.intro-copy{position:absolute;left:110px;top:18px;width:330px}
.intro-copy h1{font-size:16px;font-weight:700;font-style:italic;color:var(--ink);line-height:1.2;text-align:right;margin-bottom:14px}
.intro-copy p{font-size:7.5px;font-style:italic;line-height:1.6;color:var(--text);margin-bottom:8px}
.benefits{position:absolute;left:470px;top:18px;display:flex;gap:16px}
.benefit{width:150px}
.benefit-photo{height:60px;margin-bottom:10px}
.benefit h3{font-size:10px;font-weight:600;font-style:italic;color:var(--ink);margin-bottom:8px}
.benefit p{font-size:7px;font-style:italic;line-height:1.6;color:var(--muted)}
.ph-room-a{background:linear-gradient(180deg,#4e4b47 0%,#6d6a64 45%,#9a7b5c 100%)}
.ph-room-b{background:linear-gradient(180deg,#2f4a3e 0%,#3f5a4d 45%,#8d7358 100%)}
.ph-room-c{background:linear-gradient(100deg,#9b8a76 0%,#8a7c6c 50%,#5f5a52 100%)}

.features{position:absolute;top:500px;left:0;width:1200px;height:270px;background:var(--soft)}
.features h2{text-align:center;font-size:17px;font-weight:600;font-style:italic;color:var(--ink);margin-top:24px}
.features .lead{text-align:center;font-size:7.5px;font-style:italic;line-height:1.6;color:var(--muted);margin-top:10px}
.feature-photo{position:absolute;left:330px;top:92px;width:200px;height:160px;background:
  radial-gradient(circle at 25% 20%,rgba(74,110,50,.85),rgba(74,110,50,0) 38%),
  linear-gradient(135deg,#b79a7b 0%,#c8ad8e 62%,#3a3a3a 82%,#e8e8e8 100%)}
.feature-list{position:absolute;left:560px;top:92px;width:240px}
.feature-item{display:flex;gap:10px;margin-bottom:24px}
.feature-item svg{flex:none;width:14px;height:18px}
.feature-item h3{font-size:8px;font-weight:600;font-style:italic;color:var(--ink);margin-bottom:6px}
.feature-item p{font-size:7px;font-style:italic;line-height:1.6;color:var(--text)}
.feature-deco{position:absolute;left:900px;top:66px;width:90px;height:80px;background:radial-gradient(ellipse at 40% 40%,#f3ead3,#dcc9a0);border-radius:40% 20% 45% 25%}

.gallery{position:absolute;top:770px;left:0;width:1200px;height:69px;display:flex}
.gallery div{flex:1}
.g1{background:linear-gradient(#e2e2e2,#a8a8a8)}
.g2{background:linear-gradient(#bdb2a9,#8d8279)}
.g3{background:linear-gradient(#efefef,#9b9b9b)}
.g4{background:linear-gradient(#4a4742,#2f2d2a)}
.g5{background:linear-gradient(#2c3446,#8b6b4f)}
.g6{background:linear-gradient(#a08a74,#7a6452)}
</style>
</head>
<body>
<nav class="site-nav">
  <a href="#" class="is-active">HOME</a><a href="#">ABOUT</a><a href="#">SKILLS</a><a href="#">SERVICE</a><a href="#">WORK</a><a href="#">TESTIMONIAL</a><a href="#">BLOG</a><a href="#">TEAM</a><a href="#">CONTACT</a>
  <svg viewBox="0 0 14 14"><circle cx="6" cy="6" r="4.5" fill="none" stroke="#1f1f1f" stroke-width="1.6"/><line x1="9.3" y1="9.3" x2="13" y2="13" stroke="#1f1f1f" stroke-width="1.6"/></svg>
</nav>

<header class="hero">
  <div class="hero-photo" role="img" aria-label="Bright living room with white sofas, large window and dark wooden floor"></div>
  <div class="brand-name">BELLHAVEN</div>
  <form class="signup">
    <h2>Apply Now for Free</h2>
    <label>Your email</label><div class="field">studio@floorform.pl</div>
    <label>Your name</label><div class="field">AnnaNowicka</div>
    <label>Your phone</label><div class="field">123 456 789</div>
    <span class="cta">APPLY FOR FREE TRIAL</span>
  </form>
  <svg class="scroll-down" viewBox="0 0 12 8"><polyline points="1,1 6,6 11,1" fill="none" stroke="#fff" stroke-width="1.4"/></svg>
</header>

<section class="intro">
  <div class="intro-copy">
    <h1>This is your first amazing<br>feature and it's awesome!</h1>
    <p>Lorem ipsum dolor sit amet, consectetur adipiscing elit, sed do eiusmod tempor incididunt.</p>
    <p>Duis aute irure dolor in reprehenderit in voluptate velit esse cillum dolore eu fugiat nulla pariatur. Excepteur sint occaecat cupidatat non proident, sunt in culpa qui officia deserunt id est laborum.</p>
  </div>
  <div class="benefits">
    <article class="benefit"><div class="benefit-photo ph-room-a" role="img" aria-label="Kitchen with oak floor"></div><h3>First Benefit</h3><p>Lorem ipsum dolor sit amet, consectetur adipiscing elit, sed do</p></article>
    <article class="benefit"><div class="benefit-photo ph-room-b" role="img" aria-label="Green living room with wooden floor"></div><h3>Second Benefit</h3><p>Ut enim ad minim veniam, quis nostrud exercitation ullamco</p></article>
    <article class="benefit"><div class="benefit-photo ph-room-c" role="img" aria-label="Close-up of wooden floor boards"></div><h3>Third Benefit</h3><p>Ut enim ad minim veniam, quis nostrud exercitation ullamco</p></article>
  </div>
</section>

<section class="features">
  <h2>Features</h2>
  <p class="lead">Lorem ipsum dolor sit amet, consectetur adipiscing elit,<br>sed do eiusmod tempor incididunt ut labore et dolore</p>
  <div class="feature-photo" role="img" aria-label="Light oak floor with patterned rug and potted plant"></div>
  <div class="feature-list">
    <div class="feature-item"><svg viewBox="0 0 14 18"><rect x="4" y="1" width="6" height="5" fill="none" stroke="#555"/><circle cx="7" cy="11.5" r="5" fill="none" stroke="#555"/></svg><div><h3>Feature number 1</h3><p>Lorem ipsum dolor sit amet, consectetur adipiscing elit,<br>sed do eiusmod tempor incididunt ut labore et dolore</p></div></div>
    <div class="feature-item"><svg viewBox="0 0 14 18"><rect x="4" y="1" width="6" height="5" fill="none" stroke="#555"/><circle cx="7" cy="11.5" r="5" fill="none" stroke="#555"/></svg><div><h3>Feature number 1</h3><p>Lorem ipsum dolor sit amet, consectetur adipiscing elit,<br>sed do eiusmod tempor incididunt ut labore et dolore</p></div></div>
    <div class="feature-item"><svg viewBox="0 0 14 18"><rect x="4" y="1" width="6" height="5" fill="none" stroke="#555"/><circle cx="7" cy="11.5" r="5" fill="none" stroke="#555"/></svg><div><h3>Feature number 1</h3><p>Lorem ipsum dolor sit amet, consectetur adipiscing elit,<br>sed do eiusmod tempor incididunt ut labore et dolore</p></div></div>
  </div>
  <div class="feature-deco" role="img" aria-label="Curled light wood shaving"></div>
</section>

<section class="gallery" aria-label="Previous work">
  <div class="g1" role="img" aria-label="White hallway interior"></div>
  <div class="g2" role="img" aria-label="Textured floor close-up"></div>
  <div class="g3" role="img" aria-label="White shelving room"></div>
  <div class="g4" role="img" aria-label="Dark wooden floor"></div>
  <div class="g5" role="img" aria-label="Living room with coffee table"></div>
  <div class="g6" role="img" aria-label="Herringbone oak floor"></div>
</section>
</body>
</html>
```